Tess Marlowe Communication business card

I am starting a small, country-based business that offers writing, communication and marketing services to a wide range of clients, inner city big business, to mining, through to agriculture.

The appeal of my business is that it's mobile and flexible. It's just me, with lots of hands-on experience on construction and infrastructure projects.

I can provide the following services:

• Communication planning and management
• Issues and media management
• Marketing and communication materials
• Project management and strategy
• Government liaison
• Incident management communication
• Stakeholder management

It would be great to be able to use the elements of the business card design on other stationery.

Industry/Entity Type

Communication

Requirements
Must have
• The following information:

Tess Marlowe
M: 0427 391 864
E: tess@tmcommsmail.com

PO Box 152
Durrandale Q 4472
Nice to have
• a rural element (windmill, workboots, wheat stalk)

```html
<!DOCTYPE html>
<html lang="en">
<head>
<meta charset="utf-8">
<title>Tess Marlowe Communication – Business Card</title>
<link rel="stylesheet" href="https://fonts.googleapis.com/css2?family=Noto+Serif:wght@400;700&display=swap">
<style>
  :root {
    --page: #ffffff;
    --card-light-top: #ffffff;
    --card-light-bottom: #e6e7e9;
    --slate: #67686b;
    --amber: #fbb040;
    --ink: #231f20;
    --paper: #ffffff;
    --wheat-light: #c9cacc;
    --wheat-dark: #8d8e91;
  }
  * { margin: 0; padding: 0; box-sizing: border-box; }
  html, body {
    width: 863px;
    height: 1200px;
    overflow: hidden;
    background: var(--page);
    font-family: "Noto Serif", Georgia, serif;
  }
  .sheet { position: relative; width: 863px; height: 1200px; }

  .card {
    position: absolute;
    left: 77px;
    width: 704px;
    height: 402px;
    border-radius: 13px;
    overflow: hidden;
    box-shadow: 0 1px 4px rgba(0,0,0,0.35);
  }
  .card--front {
    top: 77px;
    background: linear-gradient(to bottom, var(--card-light-top) 20%, var(--card-light-bottom));
  }
  .card--back {
    top: 711px;
    background: var(--slate);
  }

  .wheat-art {
    position: absolute;
    border-radius: 40px 40px 4px 4px;
  }
  .card--front .wheat-art {
    left: 250px; top: 23px; width: 110px; height: 379px;
    background: linear-gradient(to bottom, var(--wheat-dark), var(--wheat-light) 45%, rgba(201,202,204,0.4));
    opacity: 0.55;
  }
  .card--back .wheat-art {
    left: 454px; top: 27px; width: 232px; height: 298px;
    background: linear-gradient(to bottom, rgba(160,161,164,0.55), rgba(140,141,144,0.25));
  }

  .brand-band {
    position: absolute;
    left: 0; top: 113px;
    width: 292px; height: 82px;
    background: var(--amber);
    display: flex;
    align-items: center;
    padding-left: 24px;
  }
  .brand-name {
    font-weight: 700;
    font-size: 17px;
    line-height: 1.1;
    color: var(--ink);
    width: 240px;
  }

  .contact {
    position: absolute;
    left: 304px; top: 111px;
    font-size: 15.5px;
    line-height: 21px;
    color: var(--ink);
    list-style: none;
  }

  .name-band {
    position: absolute;
    left: 514px; top: 113px;
    width: 190px; height: 82px;
    background: var(--slate);
    color: var(--paper);
    padding: 13px 0 0 17px;
  }
  .name-band__name { font-weight: 700; font-size: 22px; line-height: 1.15; }
  .name-band__role { font-size: 17px; line-height: 1.2; }

  .url-band {
    position: absolute;
    left: 0; top: 113px;
    width: 575px; height: 82px;
    background: var(--paper);
    display: flex;
    align-items: center;
    padding-left: 23px;
  }
  .url {
    font-size: 34px;
    color: var(--ink);
    letter-spacing: 0.2px;
  }
  .accent-block {
    position: absolute;
    left: 584px; top: 113px;
    width: 120px; height: 82px;
    background: var(--amber);
  }
</style>
</head>
<body>
<main class="sheet">
  <section class="card card--front" aria-label="Business card front">
    <div class="wheat-art" role="img" aria-label="Illustrated stalks of wheat rising through the card"></div>
    <div class="brand-band">
      <p class="brand-name">Tess Marlowe Communication</p>
    </div>
    <ul class="contact">
      <li>PO Box 152</li>
      <li>Durrandale Q 4472</li>
      <li>0427 391 864</li>
      <li>tess@tmcommsmail.com</li>
    </ul>
    <div class="name-band">
      <p class="name-band__name">Tess Marlowe</p>
      <p class="name-band__role">president</p>
    </div>
  </section>

  <section class="card card--back" aria-label="Business card back">
    <div class="wheat-art" role="img" aria-label="Faint illustrated wheat stalks"></div>
    <div class="url-band">
      <p class="url">www.tmcommsmail.com</p>
    </div>
    <div class="accent-block"></div>
  </section>
</main>
</body>
</html>
```